Consulting Company needs business card design

We need a business card design for a new consulting and business solutions company based in Bermuda called Corvane Holdings Limited. Looking for a double sided business card with one side only including the company logo thats attached and the other including contact information. Logo contains blue and turquoise colors and is fine to be on both sides of the card.
Contact Information for Business Card
Corvane Holdings Limited
P.O. Box KR318
Pemberly KR LT
Bermuda
Name: Marcus Telford
Position: Director
Telephone: 1 441 732 4590
Email: mtelford@corvane.bm
Website: www.corvane.bm

```html
<!DOCTYPE html>
<html lang="en">
<head>
<meta charset="utf-8">
<title>Corvane Holdings Limited – Business Card</title>
<link rel="stylesheet" href="https://fonts.googleapis.com/css2?family=Roboto:wght@400;500&display=swap">
<style>
  :root {
    --stage: #2e3033;
    --card-white: #ffffff;
    --card-fade: #eef0f2;
    --brand-blue: #1e9ad6;
    --brand-blue-deep: #1b86c0;
    --brand-teal: #1fb3b0;
    --ink: #333a40;
    --ink-soft: #5a6168;
    --on-blue: #e9f3f9;
  }
  * { margin: 0; padding: 0; box-sizing: border-box; }
  html, body { width: 1200px; height: 900px; overflow: hidden; }
  body {
    background: var(--stage);
    font-family: "Roboto", Arial, sans-serif;
    display: flex;
    flex-direction: column;
    align-items: center;
    justify-content: center;
    gap: 40px;
  }
  .card {
    width: 700px;
    height: 400px;
    border-radius: 22px;
    position: relative;
    overflow: hidden;
  }
  .card--front {
    background: linear-gradient(160deg, var(--card-fade) 0%, var(--card-white) 45%, var(--card-white) 100%);
  }
  .card--back {
    background: linear-gradient(160deg, var(--brand-blue) 0%, var(--brand-blue-deep) 100%);
    display: flex;
    align-items: center;
    justify-content: center;
  }
  .contact {
    position: absolute;
    left: 56px;
    top: 70px;
    color: var(--ink);
  }
  .contact__name {
    font-size: 27px;
    font-weight: 500;
    letter-spacing: 1px;
    text-transform: uppercase;
    color: var(--brand-blue);
  }
  .contact__role {
    font-size: 17px;
    color: var(--ink-soft);
    margin-top: 4px;
  }
  .contact__company {
    font-size: 19px;
    color: var(--brand-blue);
    margin-top: 14px;
  }
  .contact__address {
    font-size: 17px;
    line-height: 1.45;
    margin-top: 4px;
    font-style: normal;
  }
  .contact__lines {
    list-style: none;
    margin-top: 22px;
    font-size: 17px;
    line-height: 1.6;
  }
  .contact__lines li { display: flex; align-items: center; gap: 10px; }
  .contact__lines svg { width: 14px; height: 14px; flex: none; }
  .wordmark {
    position: absolute;
    right: 56px;
    top: 150px;
    text-align: right;
    color: var(--brand-blue);
  }
  .wordmark__name {
    font-size: 40px;
    font-weight: 500;
    letter-spacing: 2px;
    line-height: 1;
  }
  .wordmark__sub {
    font-size: 40px;
    font-weight: 500;
    font-size: 15px;
    letter-spacing: 5px;
    margin-top: 8px;
  }
  .wordmark--reverse {
    position: static;
    text-align: center;
    color: var(--on-blue);
  }
  .wordmark--reverse .wordmark__name { font-size: 56px; letter-spacing: 3px; }
  .wordmark--reverse .wordmark__sub { font-size: 20px; letter-spacing: 7px; margin-top: 10px; }
</style>
</head>
<body>
  <section class="card card--front" aria-label="Business card front">
    <div class="contact">
      <h1 class="contact__name">Marcus Telford</h1>
      <p class="contact__role">Director</p>
      <p class="contact__company">Corvane Holdings Limited</p>
      <address class="contact__address">
        P.O. Box KR318<br>
        Pemberly KR LT Bermuda
      </address>
      <ul class="contact__lines">
        <li>
          <svg viewBox="0 0 14 14" aria-hidden="true"><path d="M3 1 L5.5 1 L6.5 4 L5 5.2 Q6.5 8.5 9 9.3 L10.2 8 L13 9 L13 11.5 Q12 13 10 12.8 Q2 11 1.2 3.5 Q1.2 1.6 3 1 Z" fill="var(--brand-blue)"/></svg>
          1 441 732 4590
        </li>
        <li>
          <svg viewBox="0 0 14 14" aria-hidden="true"><rect x="1" y="3" width="12" height="8.5" rx="1" fill="none" stroke="var(--brand-blue)" stroke-width="1.4"/><path d="M1.5 3.5 L7 8 L12.5 3.5" fill="none" stroke="var(--brand-blue)" stroke-width="1.4"/></svg>
          mtelford@corvane.bm
        </li>
        <li>
          <svg viewBox="0 0 14 14" aria-hidden="true"><circle cx="7" cy="7" r="5.8" fill="none" stroke="var(--brand-blue)" stroke-width="1.3"/><ellipse cx="7" cy="7" rx="2.5" ry="5.8" fill="none" stroke="var(--brand-blue)" stroke-width="1.1"/><path d="M1.2 7 H12.8" stroke="var(--brand-blue)" stroke-width="1.1"/></svg>
          www.corvane.bm
        </li>
      </ul>
    </div>
    <div class="wordmark">
      <p class="wordmark__name">CORVANE</p>
      <p class="wordmark__sub">HOLDINGS LIMITED</p>
    </div>
  </section>

  <section class="card card--back" aria-label="Business card back">
    <div class="wordmark wordmark--reverse">
      <p class="wordmark__name">CORVANE</p>
      <p class="wordmark__sub">HOLDINGS LIMITED</p>
    </div>
  </section>
</body>
</html>
```